design a catchy flyer for my electrical buisness

need a flyer designed to attract people to my business by looking professional and offering specials

Target Market(s)

all people i want to look affordable to everyone but still keeping that professional look and feel

Industry/Entity Type

Electrical

Requirements
Must have
• NO JOB TO BIG OR SMALL
• CALL NOW FOR A FREE QUOTE 0400318726
• NO CALL OUT FEE
• same promises as uploaded pic maybe written different style
• Your neighborhood electrician
• 100% satisfaction guaranteed
• were here to help
• mention this flyer for 10% off
• specializing in house renovations, extensions, kitchen and bathroom upgrades switchboard upgrades
• Make your house safe with our RCD and smoke alarm packages
Nice to have
• modern
• proffesional
• shows trust when customers read it
Should not have
• corny slogans
• cheap look

```html
<!DOCTYPE html>
<html lang="en">
<head>
<meta charset="utf-8">
<title>Your Neighborhood Electrician – Flyer</title>
<link rel="stylesheet" href="https://fonts.googleapis.com/css2?family=Oswald:wght@400;500&family=Montserrat:wght@600;700&family=Open+Sans:ital,wght@0,400;0,600;1,700&display=swap">
<style>
  :root {
    --orange: #f58220;
    --orange-deep: #c9520e;
    --orange-light: #f9a34a;
    --charcoal: #3e3e40;
    --charcoal-dark: #2f2f31;
    --panel: #efeff1;
    --ink: #2b2b2b;
    --ink-soft: #555558;
    --white: #ffffff;
  }
  * { margin: 0; padding: 0; box-sizing: border-box; }
  html, body { width: 851px; height: 1200px; overflow: hidden; background: var(--white); }
  .flyer { position: relative; width: 851px; height: 1200px; overflow: hidden; background: var(--white); }

  .hero-photo {
    position: absolute; left: 0; top: 0; width: 851px; height: 590px;
    background: linear-gradient(160deg, var(--orange-light) 0%, var(--orange) 35%, #d7681c 65%, #8a3f14 100%);
  }
  .hero-shapes { position: absolute; left: 0; top: 0; }

  .headline { position: absolute; left: 58px; top: 62px; color: var(--white); font-family: "Oswald", sans-serif; font-weight: 500; text-transform: uppercase; transform-origin: left top; }
  .headline-top { display: block; font-size: 78px; line-height: 84px; transform: scaleX(0.8); transform-origin: left; white-space: nowrap; }
  .headline-main { display: block; font-size: 138px; line-height: 130px; transform: scaleX(0.74); transform-origin: left; white-space: nowrap; }

  .specialties { position: absolute; left: 61px; top: 288px; width: 460px; color: var(--white); font-family: "Montserrat", sans-serif; font-weight: 600; font-size: 19px; line-height: 29px; }
  .specialties strong { font-weight: 700; }

  .tagline { position: absolute; left: 61px; top: 488px; color: var(--white); font-family: "Oswald", sans-serif; font-weight: 500; font-size: 27px; letter-spacing: 0.2px; transform: scaleX(0.85); transform-origin: left; }

  .guarantee-badge { position: absolute; left: 497px; top: 380px; width: 237px; height: 237px; border-radius: 50%; background: linear-gradient(180deg, #2c2c2c 0%, #7a3a12 35%, var(--orange) 100%); border: 4px solid #4a4a4c; box-shadow: 0 4px 6px rgba(0,0,0,0.25); color: var(--white); text-align: center; font-family: "Oswald", sans-serif; font-weight: 500; text-transform: uppercase; }
  .guarantee-figure { display: block; margin-top: 40px; font-size: 84px; line-height: 92px; }
  .guarantee-word { display: block; font-size: 30px; line-height: 34px; }
  .guarantee-sub { display: block; font-size: 22px; line-height: 26px; }

  .safety-offer { position: absolute; left: 62px; top: 596px; color: var(--ink); font-family: "Montserrat", sans-serif; font-weight: 700; font-size: 20px; line-height: 28px; text-transform: uppercase; }
  .safety-offer .accent { color: var(--orange); }

  .promise-title { position: absolute; left: 61px; top: 683px; color: var(--orange); font-family: "Montserrat", sans-serif; font-weight: 700; font-size: 19px; text-transform: uppercase; }

  .promise-panel { position: absolute; left: 60px; top: 713px; width: 560px; height: 264px; background: var(--panel); padding: 18px 0 0 18px; }
  .promise-list { list-style: none; font-family: "Open Sans", sans-serif; font-size: 16.5px; line-height: 25px; color: var(--ink); }
  .promise-list li { position: relative; padding-left: 31px; }
  .promise-list li::before { content: ""; position: absolute; left: 0; top: 7px; width: 11px; height: 11px; background: var(--charcoal); }

  .discount-tile { position: absolute; left: 620px; top: 714px; width: 172px; height: 178px; background: var(--charcoal); color: var(--white); font-family: "Oswald", sans-serif; font-weight: 500; }
  .discount-figure { position: absolute; left: 22px; top: 14px; font-size: 124px; line-height: 124px; transform: scaleX(0.78); transform-origin: left; }
  .discount-percent { position: absolute; left: 110px; top: 28px; font-size: 58px; line-height: 58px; transform: scaleX(0.8); transform-origin: left; }
  .discount-off { position: absolute; left: 110px; top: 88px; font-size: 44px; line-height: 50px; transform: scaleX(0.8); transform-origin: left; }

  .call-to-action { position: absolute; left: 68px; top: 1008px; color: var(--ink-soft); font-family: "Oswald", sans-serif; font-weight: 500; font-size: 46px; line-height: 52px; text-transform: uppercase; transform: scaleX(0.86); transform-origin: left; white-space: nowrap; }
  .phone-number { position: absolute; left: 66px; top: 1056px; color: var(--orange); font-family: "Oswald", sans-serif; font-weight: 500; font-size: 94px; line-height: 94px; transform: scaleX(0.86); transform-origin: left; white-space: nowrap; }
  .no-fee { position: absolute; left: 69px; top: 1144px; color: var(--ink-soft); font-family: "Open Sans", sans-serif; font-style: italic; font-weight: 700; font-size: 15px; }

  .brand { position: absolute; left: 548px; top: 1058px; display: flex; align-items: center; gap: 14px; }
  .brand-dot { width: 36px; height: 36px; border-radius: 50%; background: var(--charcoal); }
  .brand-name { color: var(--orange); font-family: "Open Sans", sans-serif; font-weight: 400; font-size: 25px; }

  .footer-strip { position: absolute; left: 0; top: 1190px; width: 851px; height: 10px; background: var(--charcoal); }
</style>
</head>
<body>
<main class="flyer">
  <div class="hero-photo" role="img" aria-label="Modern timber-lined open-plan living room and kitchen with bar stools and an armchair, washed in warm orange light"></div>

  <svg class="hero-shapes" width="851" height="600" viewBox="0 0 851 600" aria-hidden="true">
    <polygon points="0,436 851,356 851,470 0,577" fill="var(--charcoal)"/>
    <polygon points="0,577 851,470 851,600 0,600" fill="var(--white)"/>
  </svg>

  <h1 class="headline">
    <span class="headline-top">Your Neighborhood</span>
    <span class="headline-main">Electrician</span>
  </h1>

  <p class="specialties">Specializing in <strong>HOUSE RENOVATIONS, EXTENSIONS, KITCHEN</strong> and <strong>BATHROOM UPGRADES SWITCHBOARD UPGRADES</strong></p>

  <p class="tagline">NO JOB TO BIG OR SMALL</p>

  <div class="guarantee-badge">
    <span class="guarantee-figure">100%</span>
    <span class="guarantee-word">Satisfaction</span>
    <span class="guarantee-sub">Guaranteed</span>
  </div>

  <p class="safety-offer">Make your house&nbsp; safe with<br>our <span class="accent">RCD</span> and <span class="accent">smoke alarm</span> packages</p>

  <h2 class="promise-title">Our promise to you</h2>

  <section class="promise-panel">
    <ul class="promise-list">
      <li>We will arrive on time or we will pay you $100</li>
      <li>Before any job begins you will know the exact cost</li>
      <li>We will leave your place as clean as when we arrived</li>
      <li>If there is a problem and it’s our fault we will fix it for free</li>
      <li>We will return your telephone calls promptly</li>
      <li>We will provide a 12 months warranty on all parts</li>
      <li>We will provide friendly, helpful service and advice</li>
      <li>We will provide you with a fixed price guarantee assuring on extra costs</li>
    </ul>
  </section>

  <div class="discount-tile" aria-label="10% off">
    <span class="discount-figure">10</span>
    <span class="discount-percent">%</span>
    <span class="discount-off">OFF</span>
  </div>

  <p class="call-to-action">Call now for a free quote</p>
  <p class="phone-number">040 031 8726</p>
  <p class="no-fee">No Call Out Fee</p>

  <div class="brand">
    <span class="brand-dot"></span>
    <span class="brand-name">VoltBridge</span>
  </div>

  <div class="footer-strip"></div>
</main>
</body>
</html>
```